Letterhead in Word Format

We are a small law firm in the Midwest. Our clientele is generally small business owners and companies.

We recently had a complete re-brand with a new logo, new letterhead, business cards, etc. However, the major issue now is that we cannot use the letterhead without physically ordering letterhead. Thus, invoices, and other items cannot be custom drafted.

We require custom letterhead in MICROSOFT WORD format. Our logo will be provided to you. And we will also provide a copy of the letterhead that was prepared.

We would like to see designs that are black and white, sophisticated, elegant, and generally professional. We prefer a traditional design with just a touch of contemporary.

Please do not submit any designs that are not Microsoft Word compatible.

EDIT: Please view the attached letterhead. The design must include the logo, name, address, fax, phone, email, and name of attorney.
Updates

Thank you all for submitting designs. I just wanted to quickly provide some feedback. I saw a few designs that had the logo at the bottom. Because there will be text with margins at 1" all around, it's not practical have the logo at the bottom. Also, designs with blocks of gray or black would cause our printer to bleed black onto the letterhead, so that is not practical as well.

If you have any comments, please feel free to leave me a message. Thank you.

Target Market(s)

Small business owners, companies, real estate investors and developers.

Industry/Entity Type

Small Business

Font styles to use
Script

Requirements
Must have
• Microsoft Word Format

```html
<!DOCTYPE html>
<html lang="en">
<head>
<meta charset="utf-8">
<title>Mercer Legal Group — Letterhead</title>
<link href="https://fonts.googleapis.com/css2?family=Cormorant+Garamond:wght@500;600&family=Gelasio:wght@400;700&display=swap" rel="stylesheet">
<style>
  :root {
    --ink: #4a4a4a;
    --ink-dark: #1e1e1e;
    --ink-muted: #7a7a7a;
    --paper: #ffffff;
    --band: #3b3b3b;
    --band-text: #ffffff;
    --signature-tone: #e6e6e6;
  }
  * { margin: 0; padding: 0; box-sizing: border-box; }
  html, body { width: 852px; height: 1200px; overflow: hidden; background: var(--paper); }
  .letterhead {
    position: relative; width: 852px; height: 1200px;
    background: var(--paper); color: var(--ink);
    font-family: "Gelasio", Georgia, serif;
  }
  .firm-name {
    position: absolute; left: 99px; top: 110px;
    font-family: "Gelasio", Georgia, serif;
    font-weight: 400; font-size: 33px;
    color: var(--ink-dark); line-height: 1;
  }
  .attorney {
    position: absolute; right: 85px; top: 92px; text-align: right;
    font-family: "Cormorant Garamond", serif; color: var(--ink-dark);
    font-variant-numeric: lining-nums;
  }
  .attorney-name { font-size: 11.5px; font-weight: 600; text-transform: uppercase; letter-spacing: 0.2px; }
  .attorney-title { font-size: 10px; color: var(--ink-muted); margin-top: 3px; }
  .attorney-contact { font-size: 11px; margin-top: 16px; line-height: 1.3; }
  .attorney-contact b { font-weight: 600; }
  .letter { position: absolute; left: 111px; width: 656px; font-size: 16.4px; }
  .letter-date { top: 288px; }
  .recipient { top: 331px; line-height: 23px; font-style: normal; }
  .recipient-name { font-weight: 700; }
  .letter-body { top: 423px; line-height: 22.7px; text-align: justify; }
  .letter-body p + p { margin-top: 22.7px; }
  .closing { top: 852px; }
  .signature-mark {
    position: absolute; left: 92px; top: 877px; width: 172px; height: 40px;
    background: var(--signature-tone); border-radius: 4px;
  }
  .signer { top: 921px; }
  .footer-band {
    position: absolute; left: 0; bottom: 0; width: 852px; height: 41px;
    background: var(--band); color: var(--band-text);
    font-size: 11px; display: flex; align-items: center; justify-content: center; gap: 18px;
  }
  .footer-band b { font-weight: 700; }
  .divider { opacity: 0.8; }
</style>
</head>
<body>
<main class="letterhead">
  <header>
    <div class="firm-name">Mercer Legal Group</div>
    <div class="attorney">
      <div class="attorney-name">Rowan B. Mercer</div>
      <div class="attorney-title">Principal Attorney</div>
      <div class="attorney-contact">
        <div><b>Phone:</b> (708)555-0142</div>
        <div><b>Fax:</b> (708) 555-0143</div>
      </div>
    </div>
  </header>

  <div class="letter letter-date">January 26, 2014</div>

  <address class="letter recipient">
    <div class="recipient-name">Elena Marsh</div>
    <div>General Manager</div>
    <div>Northgate Supply Co</div>
  </address>

  <section class="letter letter-body">
    <p>Lorem ipsum dolor sit amet, consectetur adipiscing elit. Donec orci purus, luctus vitae dignissim eu, iaculis sed purus. Vivamus faucibus, ipsum nec aliquet viverra, leo mauris condimentum ligula, sit amet sagittis enim ligula quis arcu. Nam egestas tortor id nisi porttitor mattis. In tortor ante, ultricies in suscipit a, tempus non massa. Vivamus et auctor mi. Fusce vel massa nulla. Phasellus nec eros mauris, et scelerisque orci. Donec malesuada orci vitae nulla accumsan porta a id massa. Quisque accumsan iaculis magna sit amet fringilla. Maecenas consequat, magna eget tincidunt semper, odio nibh rutrum mi, id feugiat ante nisi eu risus. Vestibulum nunc orci, ultricies in mi.</p>
    <p>Quisque scelerisque sagittis nulla at porttitor. Mauris a justo et tellus interdum tristique. Sed id augue vitae urna euismod commodo aliquet a quam. Pellentesque arcu velit, cursus et malesuada ut, rutrum nisi iaculis consequat et diam. Nullam erat sem, rhoncus id ullamcorper vitae, rhoncus et arcu. In ultricies ultricies nulla, ut rutrum nisi iaculis at. Donec eu magna a metus ornare faucibus. Fusce aliquet faucibus ultricies. Morbi semper, est id tincidunt gravida, sem arcu adipiscing lacus, ac bibendum nulla leo eu purus. Quisque nec diam sed risus consectetur a ccumsan quis quis nibh. Vestibulum id purus lorem.</p>
  </section>

  <div class="letter closing">Ipsum dolor,</div>
  <div class="signature-mark" role="img" aria-label="Handwritten signature of the sender"></div>
  <div class="letter signer">Daniel Avery Hale</div>

  <footer class="footer-band">
    <span><b>Address:</b> 2210 W. Harlow Ave., Westbrook, Illinois 60199</span>
    <span class="divider">|</span>
    <span><b>Web:</b> www.mercerlegalgroup.com</span>
    <span class="divider">|</span>
    <span>Email: rbm@mercerlegalgroup.com</span>
  </footer>
</main>
</body>
</html>
```